Brand new website for global research and investment startup

We need a simple website, maybe 3 pages: landing page with business description, investment philosophy, team and contact info.
We have a logo already that can be incorporated. Please use the logo only, not the text
We like the color green, something along the lines of #3D6C32 as the main color.
We'd like to design the website with geometric shapes in gradations of the base color. The shapes should suggest "work in progress", "built to last (a long time)", "solidity" and "indestructibility". One idea floating in my head sees smaller features with icosahedron and dodecahedron shapes, and maybe larger structures like crystal lattices; but please feel free to be creative and imagine your own.

```html
<!DOCTYPE html>
<html lang="en">
<head>
<meta charset="utf-8">
<title>Verdant Meridian — Research-driven investing</title>
<link href="https://fonts.googleapis.com/css2?family=Cormorant+Garamond:wght@400;500&family=Poppins:wght@400;500;600&display=swap" rel="stylesheet">
<style>
  :root {
    --green: #3d6c32;
    --green-dark: #2e5426;
    --green-deep: #1b2e17;
    --green-soft: #eaf1e8;
    --green-mist: #dfeadb;
    --ink: #1d1d1d;
    --muted: #444;
    --white: #ffffff;
    --line: #c9d6c5;
  }
  * { box-sizing: border-box; margin: 0; padding: 0; }
  html, body { width: 1200px; height: 2899px; overflow: hidden; }
  body {
    position: relative;
    background: var(--white);
    font-family: "Poppins", sans-serif;
    color: var(--ink);
  }
  .abs { position: absolute; }
  .serif { font-family: "Cormorant Garamond", serif; font-weight: 400; }

  /* Header */
  .site-header { left: 0; top: 0; width: 1200px; height: 79px; background: var(--white); }
  .brand { left: 150px; top: 26px; display: flex; align-items: center; gap: 10px;
    font-size: 17px; font-weight: 600; color: var(--green); }
  .brand-mark { width: 20px; height: 20px; background: var(--green); }
  .main-nav { left: 465px; top: 33px; display: flex; gap: 23px; font-size: 12px; font-weight: 500; }
  .phone-btn { left: 900px; top: 20px; width: 149px; height: 39px; background: var(--green);
    color: var(--white); font-size: 11px; font-weight: 600; display: flex; align-items: center;
    justify-content: center; gap: 7px; }

  /* Hero */
  .hero { left: 0; top: 79px; width: 1200px; height: 465px;
    background: linear-gradient(100deg, #e3ecdf 0%, #f2f6f0 35%, #eef4eb 70%, #dbe7d6 100%); }
  .hero-art { left: 473px; top: 80px; width: 640px; height: 390px;
    background: radial-gradient(ellipse at 55% 55%, #3d6c32 0%, #6b9a5d 30%, rgba(200,220,192,.5) 60%, rgba(238,244,235,0) 75%); }
  .hero-title { left: 148px; top: 168px; font-size: 56px; line-height: 50px; color: var(--green-dark); letter-spacing: .5px; }
  .hero-lead { left: 150px; top: 333px; width: 320px; font-size: 13px; line-height: 19px; }
  .btn { height: 39px; font-size: 11px; font-weight: 600; letter-spacing: 1px;
    display: flex; align-items: center; justify-content: center; }
  .btn-solid { left: 150px; top: 406px; width: 124px; background: var(--green); color: var(--white); }
  .btn-ghost { left: 280px; top: 406px; width: 125px; border: 1px solid var(--green); color: var(--green); }

  /* Section titles */
  .section-title { left: 0; width: 1200px; text-align: center; font-size: 44px; line-height: 42px;
    color: var(--green-dark); text-transform: uppercase; }

  /* Philosophy cards */
  .principle { width: 260px; border: 1px solid var(--green); border-radius: 10px; background: var(--white);
    text-align: center; }
  .principle-icon { position: absolute; left: 96px; width: 67px; height: 67px; border-radius: 50%; background: var(--green); }
  .principle h3 { position: absolute; left: 0; width: 100%; font-size: 23px; color: var(--green); }
  .principle p { position: absolute; left: 35px; width: 188px; font-size: 11.5px; line-height: 15px; }
  .principle-bar { position: absolute; bottom: -4px; height: 7px; border-radius: 4px; background: var(--green); }

  /* Values band */
  .values-band { left: 0; top: 1058px; width: 1200px; height: 730px;
    background: linear-gradient(180deg, var(--green-soft) 0%, var(--green-soft) 55%, #ffffff 100%);
    clip-path: polygon(0 48px, 810px 48px, 872px 0, 1200px 0, 1200px 100%, 0 100%); }
  .hex-grid { left: 0; top: 1170px; }

  /* Team */
  .team-card { width: 287px; height: 264px; border-radius: 22px; background: var(--white);
    box-shadow: 0 8px 30px rgba(0,0,0,.08); text-align: center; }
  .avatar { position: absolute; left: 107px; top: 42px; width: 72px; height: 72px; border-radius: 50%;
    background: linear-gradient(160deg, #9aa3a8, #4b5357); }
  .team-card h3 { position: absolute; top: 120px; width: 100%; font-size: 26px; color: var(--green-dark); }
  .team-role { position: absolute; top: 156px; width: 100%; font-size: 10px; color: var(--muted); text-transform: uppercase; }
  .team-bio { position: absolute; top: 179px; left: 55px; width: 177px; font-size: 11.5px; line-height: 15px; }
  .slider-btn { width: 45px; height: 45px; border-radius: 50%; border: 1px solid var(--green);
    display: flex; align-items: center; justify-content: center; }

  .lower-bg { left: 0; top: 2100px; width: 1200px; height: 695px;
    background: linear-gradient(180deg, #ffffff 0%, #f4f5f4 50%, #f1f2f1 100%); }

  /* Contact */
  .contact-photo { left: 150px; top: 2243px; width: 449px; height: 485px; border-radius: 34px 34px 34px 34px;
    background: linear-gradient(135deg, #7a4a2c 0%, #b7866a 35%, #9aa8b6 60%, #2e3a52 100%); }
  .contact-panel { left: 599px; top: 2285px; width: 449px; height: 402px; background: var(--green);
    border-radius: 0 34px 34px 0; color: var(--white); }
  .contact-title { left: 634px; top: 2310px; font-size: 46px; color: var(--white); }
  .contact-lead { left: 634px; top: 2366px; width: 340px; font-size: 12px; line-height: 17px; color: var(--white); }
  .field { font-size: 10.5px; color: var(--white); border-bottom: 1px solid rgba(255,255,255,.85); padding-bottom: 4px; }
  .submit { left: 634px; top: 2607px; width: 124px; height: 39px; background: var(--green-deep); color: var(--white);
    font-size: 11px; font-weight: 600; letter-spacing: 1px; display: flex; align-items: center; justify-content: center; }

  /* Footer */
  .site-footer { left: 0; top: 2795px; width: 1200px; height: 104px; background: var(--green); color: var(--white);
    text-align: center; }
  .footer-nav { position: absolute; top: 36px; width: 100%; font-size: 12px; font-weight: 600; }
  .copyright { position: absolute; top: 56px; width: 100%; font-size: 11px; }
</style>
</head>
<body>

<header class="site-header abs">
  <div class="brand abs"><span class="brand-mark"></span>Verdant Meridian</div>
  <nav class="main-nav abs"><span>HOME</span><span>PHILOSOPHY</span><span>TEAM</span><span>CONTACT</span></nav>
  <div class="phone-btn abs">
    <svg width="14" height="14" viewBox="0 0 24 24" fill="none" stroke="#fff" stroke-width="2"><path d="M22 16.9v3a2 2 0 0 1-2.2 2 19.8 19.8 0 0 1-8.6-3.1 19.5 19.5 0 0 1-6-6A19.8 19.8 0 0 1 2.1 4.2 2 2 0 0 1 4.1 2h3a2 2 0 0 1 2 1.7c.1.9.4 1.8.7 2.7a2 2 0 0 1-.5 2.1L8 9.8a16 16 0 0 0 6 6l1.3-1.3a2 2 0 0 1 2.1-.4c.9.3 1.8.6 2.7.7a2 2 0 0 1 1.7 2z"/></svg>
    +1 (415) 555-0142
  </div>
</header>

<section class="hero abs"></section>
<div class="hero-art abs" role="img" aria-label="Green faceted crystal star within a lattice of connected nodes"></div>
<h1 class="hero-title abs serif">Research-driven<br>investing built for<br>generations.</h1>
<p class="hero-lead abs">We are a global research and investment firm committed to compounding knowledge, capital, and conviction over the long term.</p>
<a class="btn btn-solid abs">LEARN MORE</a>
<a class="btn btn-ghost abs">CONTACT US</a>

<h2 class="section-title abs serif" style="top:614px">Our Investment<br>Philosophy</h2>

<div class="principle abs" style="left:197px;top:749px;height:249px">
  <span class="principle-icon" style="top:51px"><svg width="67" height="67" viewBox="0 0 67 67" fill="none" stroke="#fff" stroke-width="1"><polygon points="33.5,14 50,24 50,43 33.5,53 17,43 17,24"/><polygon points="33.5,22 43,39 24,39"/><line x1="33.5" y1="14" x2="33.5" y2="22"/><line x1="17" y1="43" x2="24" y2="39"/><line x1="50" y1="43" x2="43" y2="39"/></svg></span>
  <h3 class="serif" style="top:122px">Independent Research</h3>
  <p style="top:160px">We invest only where conviction comes from original analysis and deep understanding.</p>
  <span class="principle-bar" style="left:105px;width:50px"></span>
</div>
<div class="principle abs" style="left:470px;top:729px;height:269px">
  <span class="principle-icon" style="top:60px"><svg width="67" height="67" viewBox="0 0 67 67" fill="none" stroke="#fff" stroke-width="1"><circle cx="33.5" cy="33.5" r="18"/><polygon points="33.5,21 45,29.5 41,43 26,43 22,29.5"/></svg></span>
  <h3 class="serif" style="top:130px">Long-Term Thinking</h3>
  <p style="top:164px">Capital is allocated with decades- not quarters-in mind. We focus on enduring value.</p>
  <span class="principle-bar" style="left:94px;width:72px"></span>
</div>
<div class="principle abs" style="left:743px;top:749px;height:249px">
  <span class="principle-icon" style="top:51px"><svg width="67" height="67" viewBox="0 0 67 67" fill="none" stroke="#fff" stroke-width="1"><polygon points="33.5,14 50,24 50,43 33.5,53 17,43 17,24"/><polygon points="33.5,24 42,38 25,38"/><polygon points="33.5,43 25,29 42,29"/></svg></span>
  <h3 class="serif" style="top:122px">Disciplined Execution</h3>
  <p style="top:160px">Risk management and patience remain fundamental to every investment we make.</p>
  <span class="principle-bar" style="left:105px;width:50px"></span>
</div>

<div class="values-band abs"></div>
<svg class="hex-grid abs" width="1200" height="560" viewBox="0 0 1200 560" font-family="Cormorant Garamond, serif" font-size="16" fill="#fff" text-anchor="middle">
  <g stroke="#fff" stroke-width="3">
    <polygon fill="#3d6c32" points="409,6 503,60 503,168 409,222 315,168 315,60"/>
    <polygon fill="#2e5426" points="600,6 694,60 694,168 600,222 506,168 506,60"/>
    <polygon fill="#3d6c32" points="791,6 885,60 885,168 791,222 697,168 697,60"/>
    <polygon fill="#2e5426" points="504,170 598,224 598,332 504,386 410,332 410,224"/>
    <polygon fill="#2e5426" points="696,170 790,224 790,332 696,386 602,332 602,224"/>
    <polygon fill="#3d6c32" points="600,334 694,388 694,496 600,550 506,496 506,388"/>
  </g>
  <text x="409" y="101">RESEARCH-DRIVEN</text><text x="409" y="121">INVESTMENT</text><text x="409" y="141">STRATEGY</text>
  <text x="600" y="112">LONG-TERM VALUE</text><text x="600" y="132">CREATION</text>
  <text x="791" y="101">DISCIPLINED</text><text x="791" y="121">RISK</text><text x="791" y="141">MANAGEMENT</text>
  <text x="504" y="274">INDEPENDENT</text><text x="504" y="294">THINKING</text>
  <text x="696" y="265">GLOBAL</text><text x="696" y="285">INVESTMENT</text><text x="696" y="305">PERSPECTIVE</text>
  <text x="600" y="438">TRUSTED</text><text x="600" y="458">PARTNERSHIP</text>
</svg>

<div class="lower-bg abs"></div>

<h2 class="section-title abs serif" style="top:1782px">Meet Our Team</h2>

<div class="team-card abs" style="left:156px;top:1853px">
  <span class="avatar" role="img" aria-label="Portrait of the founder"></span>
  <h3 class="serif">Elliot Marsh</h3>
  <div class="team-role">Founder &amp; CIO</div>
  <p class="team-bio">20+ years of global investing experience across public and private markets.</p>
</div>
<div class="team-card abs" style="left:457px;top:1853px">
  <span class="avatar" role="img" aria-label="Portrait of the head of research"></span>
  <h3 class="serif">Dr. Lena Ortiz</h3>
  <div class="team-role">Head of Research</div>
  <p class="team-bio">Leads our research platform with a focus on fundamental and quantitative analysis.</p>
</div>
<div class="team-card abs" style="left:756px;top:1853px">
  <span class="avatar" role="img" aria-label="Portrait of the portfolio manager"></span>
  <h3 class="serif">Samuel Reyes</h3>
  <div class="team-role">Portfolio Manager</div>
  <p class="team-bio">Focused on long-term compounding and capital allocation discipline.</p>
</div>

<span class="slider-btn abs" style="left:552px;top:2151px"><svg width="12" height="12" viewBox="0 0 12 12" fill="none" stroke="#3d6c32" stroke-width="1.4"><polyline points="8,1 3,6 8,11"/></svg></span>
<span class="slider-btn abs" style="left:603px;top:2151px"><svg width="12" height="12" viewBox="0 0 12 12" fill="none" stroke="#3d6c32" stroke-width="1.4"><polyline points="4,1 9,6 4,11"/></svg></span>

<div class="contact-panel abs"></div>
<div class="contact-photo abs" role="img" aria-label="Support staff with headsets working at computers in a warm office"></div>
<h2 class="contact-title abs serif">Contact us</h2>
<p class="contact-lead abs">We welcome like-minded partners who share our commitment to rigorous research and long-term value creation.</p>
<div class="field abs" style="left:634px;top:2444px;width:180px">First Name</div>
<div class="field abs" style="left:832px;top:2444px;width:180px">Last Name</div>
<div class="field abs" style="left:634px;top:2493px;width:180px">Email</div>
<div class="field abs" style="left:832px;top:2493px;width:180px">Phone</div>
<div class="field abs" style="left:634px;top:2558px;width:378px">Message</div>
<a class="submit abs">SUBMIT</a>

<footer class="site-footer abs">
  <div class="footer-nav">HOME &nbsp;|&nbsp; PHILOSOPHY &nbsp;|&nbsp; TEAM &nbsp;|&nbsp; CONTACT</div>
  <div class="copyright">Copyright © 2026 VERDANT MERIDIAN. All rights reserved.</div>
</footer>

</body>
</html>
```